Home care agency

Current website QTRBLOOMS.com. Need to update and reformat to different pages. use my info from my current website

Target Market(s)

adult children

Industry/Entity Type

Home Health

Coding

Coded - Design and coding required

Number of Pages Required

4 page

Font styles to use
Sans Serif

Colors
3276b5
33a6d7
3277b5
85cae6
85acd3

```html
<!DOCTYPE html>
<html lang="en">
<head>
<meta charset="utf-8">
<title>Hearthside Home Health Services</title>
<link href="https://fonts.googleapis.com/css2?family=Roboto:wght@300;400;500;700&display=swap" rel="stylesheet">
<style>
:root{
  --blue:#3276b5;
  --blue-2:#3277b5;
  --sky:#33a6d7;
  --light:#85cae6;
  --soft:#85acd3;
  --hero:#8ccbe8;
  --ink:#2b2b2b;
  --text:#777;
  --grey:#f5f5f5;
  --footer:#2c2c2c;
  --white:#fff;
}
*{box-sizing:border-box;margin:0;padding:0}
html,body{width:1200px;height:4412px;overflow:hidden}
body{font-family:"Roboto",Arial,sans-serif;color:var(--ink);background:var(--white);position:relative}
.abs{position:absolute}
.wrap{position:absolute;left:160px;width:880px}
.eyebrow{font-size:12px;letter-spacing:2px;text-transform:uppercase;color:var(--text)}
.title{font-size:36px;font-weight:700;color:var(--ink)}
.title span{color:var(--blue)}
.p{font-size:13px;line-height:22px;color:var(--text)}
.btn{display:inline-block;border-radius:30px;font-size:12px;font-weight:700;padding:10px 24px;text-transform:uppercase}
.photo{position:absolute}

/* header */
.site-header{position:absolute;top:0;left:0;width:1200px;height:112px;background:var(--white);box-shadow:0 2px 6px rgba(0,0,0,.08)}
.brand{position:absolute;left:160px;top:26px;display:flex;align-items:center;gap:10px;font-size:15px;font-weight:700;color:var(--blue)}
.brand i{width:56px;height:56px;border-radius:50%;border:2px solid var(--blue);display:block}
.quote-link{position:absolute;right:100px;top:0;background:#f0f0f0;font-size:11px;font-weight:700;padding:10px 20px}
.nav{position:absolute;right:160px;top:60px;display:flex;gap:6px}
.nav a{font-size:12px;font-weight:500;padding:8px 12px;color:var(--ink)}
.nav a.on{background:var(--blue);color:var(--white)}

/* hero */
.hero{position:absolute;top:112px;left:0;width:1200px;height:448px;background:var(--hero)}
.hero .eyebrow{color:var(--white);position:absolute;left:162px;top:124px;font-size:14px}
.hero h1{position:absolute;left:162px;top:146px;width:380px;font-size:30px;line-height:36px;color:var(--white);font-weight:700}
.hero .p{position:absolute;left:162px;top:222px;width:360px;color:var(--white);font-size:12px;line-height:18px}
.hero .btn{position:absolute;left:162px;top:286px;background:var(--white);color:var(--blue);padding:8px 18px}
.arrow{position:absolute;top:190px;width:26px;height:70px;background:rgba(0,0,0,.2)}

/* about */
.about .eyebrow{top:624px}
.about .title{position:absolute;top:640px}
.about .bar{position:absolute;top:692px;width:60px;height:3px;background:var(--blue)}
.about .p{position:absolute;top:712px;width:400px}

/* services */
.services{position:absolute;top:1015px;left:0;width:1200px;height:685px;background:var(--blue)}
.center{position:absolute;left:0;width:1200px;text-align:center}
.services .eyebrow,.services .title{color:var(--white)}
.tabs{position:absolute;top:167px;left:0;width:1200px;display:flex;justify-content:center;gap:14px}
.tabs span{font-size:11px;font-weight:700;color:var(--white);padding:8px 14px;border-radius:20px}
.tabs span.on{background:var(--white);color:var(--blue)}
.card{position:absolute;width:280px;height:148px;border:1px solid rgba(255,255,255,.6);padding:16px 18px 0 62px;color:var(--white)}
.card.on{background:var(--white);color:var(--ink)}
.card svg{position:absolute;left:18px;top:16px}
.card h3{font-size:15px;font-weight:500;line-height:18px;margin-bottom:8px}
.card p{font-size:11px;line-height:15px;opacity:.85}
.card b{display:block;font-size:10px;margin-top:8px}
.services .btn{position:absolute;top:603px;left:520px;border:1px solid var(--white);color:var(--white)}

/* why */
.why .col{position:absolute;top:1752px;width:260px}
.why .col svg{position:absolute;left:0;top:0}
.why h4{margin-left:70px;font-size:16px;font-weight:500;margin-bottom:12px;margin-top:10px}
.why .p{margin-left:70px;font-size:11px;line-height:17px}
.why li{list-style:none;margin-left:70px;font-size:11px;line-height:17px;color:var(--text);margin-bottom:14px;position:relative}
.why li:before{content:"";position:absolute;left:-16px;top:6px;width:6px;height:6px;border-radius:50%;background:var(--blue)}

/* testimonials */
.testimonials{position:absolute;top:2072px;left:0;width:1200px;height:383px;background:var(--grey)}
.dots{position:absolute;left:1028px;top:228px}
.dots i{display:block;width:8px;height:8px;border-radius:50%;background:var(--blue);margin-bottom:12px}

/* consult */
.consult{position:absolute;top:2455px;left:0;width:603px;height:641px;background:var(--blue);color:var(--white)}
.consult .field{position:absolute;height:38px;border-bottom:1px solid rgba(255,255,255,.5);font-size:11px;padding-top:12px}
.consult .legend{position:absolute;left:162px;width:400px;font-size:10px;font-weight:700;letter-spacing:1px;border-top:1px solid rgba(255,255,255,.5);border-bottom:1px solid rgba(255,255,255,.5);padding:5px 10px}
.stat{position:absolute;top:2950px;height:107px;background:var(--light);color:var(--white);text-align:center;padding-top:20px}
.stat b{display:block;font-size:34px}
.stat span{font-size:11px}

/* blog */
.post{position:absolute;top:3257px;width:280px;height:373px;background:var(--white);box-shadow:0 2px 8px rgba(0,0,0,.1)}
.post .img{position:absolute;left:0;top:0;width:280px;height:206px}
.post .date{position:absolute;left:0;top:0;width:56px;height:56px;background:var(--blue);color:var(--white);text-align:center;font-size:18px;font-weight:700;padding-top:8px}
.post .date small{display:block;font-size:9px;font-weight:400}
.post h3{position:absolute;left:16px;top:222px;width:250px;font-size:14px;line-height:18px;font-weight:700}
.post .p{position:absolute;left:16px;top:264px;width:250px;font-size:10px;line-height:14px}
.post .btn{position:absolute;left:16px;top:326px;background:var(--blue);color:var(--white);font-size:10px;padding:7px 14px}
.post .meta{position:absolute;left:150px;top:334px;font-size:10px;color:var(--text)}

/* cta */
.cta{position:absolute;top:3793px;left:0;width:1200px;height:205px;background:var(--blue)}
.cta-box{position:absolute;left:491px;top:44px;width:544px;height:118px;border:2px solid var(--white);color:var(--white);padding:22px 28px;font-size:14px;line-height:20px}
.cta-box b{font-size:17px}
.cta-box .btn{position:absolute;right:30px;top:38px;background:var(--white);color:var(--blue)}

/* footer */
.site-footer{position:absolute;top:3998px;left:0;width:1200px;height:414px;background:var(--footer);color:#ccc}
.fcol{position:absolute;top:56px;width:200px;font-size:11px;line-height:20px}
.fcol h5{color:var(--white);font-size:14px;font-weight:700;margin-bottom:12px}
.sub-input{width:160px;height:28px;border:1px solid #777;border-radius:14px;margin:8px 0;padding:6px 12px;font-size:10px}
.fbar{position:absolute;left:160px;top:316px;width:880px;border-top:1px solid #444;padding-top:14px;font-size:11px}
.social{position:absolute;right:0;top:8px;display:flex;gap:8px}
.social i{width:26px;height:26px;border-radius:50%;border:1px solid #ccc;display:block}
</style>
</head>
<body>

<header class="site-header">
  <div class="brand"><i></i>Hearthside Home Health</div>
  <div class="quote-link">GET A QUOTE ▸</div>
  <nav class="nav"><a class="on">HOME</a><a>ABOUT US</a><a>SERVICES</a><a>TESTIMONIALS</a><a>BLOG</a><a>CONTACT</a></nav>
</header>

<section class="hero">
  <div class="eyebrow">Welcome to</div>
  <h1>Providing Care Throughout the South Shore</h1>
  <p class="p">Hearthside Home Health Services is owned and operated by Marissa Dalton. Marissa is a registered nurse and has been in the health care system since 2001.</p>
  <a class="btn">Read more</a>
  <div class="photo" role="img" aria-label="Smiling nurse in white coat seated in armchair" style="left:600px;top:40px;width:370px;height:408px;background:linear-gradient(180deg,#a9d6ec,#e9eef2 55%,#2f6a8a)"></div>
  <div class="arrow" style="left:0"></div><div class="arrow" style="right:0"></div>
</section>

<section class="about">
  <div class="wrap eyebrow" style="top:618px">Since 2001 · PO Box 412 Harbor, MA 02000</div>
  <div class="wrap"><h2 class="title" style="top:640px;position:absolute">About <span>Us</span></h2></div>
  <div class="wrap"><div class="bar" style="left:0"></div>
    <div class="p" style="position:absolute;top:712px;width:400px">Hearthside Home Health Services is owned and operated by Marissa Dalton, a registered nurse who has been in the health care system since 2001. She has specialized in home care, cardiology, nursing and critical care. She holds a nursing degree and completed advanced study in health programs.<br><br>At Hearthside our caregivers have extensive background checks and training to meet every need. We incorporate the care of our clients in order to provide the best care possible in their own home. Every nurse ensures full access and understanding of client care at all times, with a dedicated staff in the client's home and a clear plan set along with the family.</div>
  </div>
  <div class="photo" role="img" aria-label="Caregiver helping senior walk" style="left:612px;top:623px;width:198px;height:171px;background:linear-gradient(135deg,#c9dbe8,#8fb3cf)"></div>
  <div class="photo" role="img" aria-label="Nurse talking with elderly woman" style="left:836px;top:623px;width:204px;height:171px;background:linear-gradient(135deg,#e4d8cc,#b9a796)"></div>
  <div class="photo" role="img" aria-label="Caregiver with senior in wheelchair" style="left:612px;top:808px;width:198px;height:162px;background:linear-gradient(135deg,#d6e5ee,#7fa9c6)"></div>
  <div class="photo" role="img" aria-label="Nurse assisting patient at home" style="left:836px;top:808px;width:204px;height:162px;background:linear-gradient(135deg,#e6e1da,#a8b6c0)"></div>
</section>

<section class="services">
  <div class="center eyebrow" style="top:70px;color:#fff">Featured Services</div>
  <div class="center title" style="top:92px;color:#fff;font-size:30px">Our Services</div>
  <div class="tabs"><span class="on">SKILLED CARE SERVICES</span><span>NON MEDICAL SERVICES</span><span>CLIENT BENEFITS</span></div>
  <div class="card on" style="left:162px;top:220px">
    <svg width="30" height="30" viewBox="0 0 30 30" fill="none" stroke="#3276b5" stroke-width="2"><rect x="5" y="3" width="20" height="24" rx="2"/><path d="M10 10h10M10 15h10M10 20h6"/></svg>
    <h3>Free Initial Nursing Assessment</h3><p>Lorem ipsum dolor sit amet, consectetur adipiscing elit, sed do eiusmod tempor incididunt ut labore.</p><b>READ MORE</b></div>
  <div class="card" style="left:462px;top:220px">
    <svg width="30" height="30" viewBox="0 0 30 30" fill="none" stroke="#fff" stroke-width="2"><rect x="4" y="10" width="22" height="10" rx="5"/><path d="M15 10v10"/></svg>
    <h3>Medication Management</h3><p>Lorem ipsum dolor sit amet, consectetur adipiscing elit, sed do eiusmod tempor incididunt ut labore.</p><b>READ MORE</b></div>
  <div class="card" style="left:760px;top:220px">
    <svg width="30" height="30" viewBox="0 0 30 30" fill="none" stroke="#fff" stroke-width="2"><path d="M15 26s-10-6-10-13a5 5 0 0 1 10-2 5 5 0 0 1 10 2c0 7-10 13-10 13z"/></svg>
    <h3>Wound Care</h3><p>Lorem ipsum dolor sit amet, consectetur adipiscing elit, sed do eiusmod tempor incididunt ut labore.</p><b>READ MORE</b></div>
  <div class="card" style="left:162px;top:390px">
    <svg width="30" height="30" viewBox="0 0 30 30" fill="none" stroke="#fff" stroke-width="2"><path d="M6 24l12-12M14 8l8 8M20 4l6 6M4 26l3-3"/></svg>
    <h3>Injections</h3><p>Lorem ipsum dolor sit amet, consectetur adipiscing elit, sed do eiusmod tempor incididunt ut labore.</p><b>READ MORE</b></div>
  <div class="card" style="left:462px;top:390px">
    <svg width="30" height="30" viewBox="0 0 30 30" fill="none" stroke="#fff" stroke-width="2"><path d="M12 4h6v8h8v6h-8v8h-6v-8H4v-6h8z"/></svg>
    <h3>Medical Care Assistance</h3><p>Lorem ipsum dolor sit amet, consectetur adipiscing elit, sed do eiusmod tempor incididunt ut labore.</p><b>READ MORE</b></div>
  <div class="card" style="left:760px;top:390px">
    <svg width="30" height="30" viewBox="0 0 30 30" fill="none" stroke="#fff" stroke-width="2"><rect x="3" y="9" width="18" height="12"/><path d="M21 13h4l3 4v4h-7"/><circle cx="9" cy="23" r="2"/><circle cx="23" cy="23" r="2"/></svg>
    <h3>Transportation to Medical Appointments</h3><p>Lorem ipsum dolor sit amet, consectetur adipiscing elit, sed do eiusmod tempor.</p><b>READ MORE</b></div>
  <a class="btn">View all services</a>
</section>

<section class="why">
  <div class="col" style="left:162px">
    <svg width="54" height="54"><circle cx="27" cy="27" r="26" fill="#e3f2fa"/><text x="27" y="34" text-anchor="middle" font-size="20" fill="#33a6d7" font-family="Roboto,sans-serif">?</text></svg>
    <h4>Why Choose Home Care?</h4>
    <p class="p">Home care is a cost-effective option that allows clients the ability to receive services in the comfort of their own home.<br><br>Home care also provides peace of mind to a family, letting them go about their day knowing a loved one is safe and cared for.</p>
  </div>
  <div class="col" style="left:462px">
    <svg width="54" height="54"><circle cx="27" cy="27" r="26" fill="#e3f2fa"/><circle cx="27" cy="27" r="11" fill="none" stroke="#33a6d7" stroke-width="2"/><path d="M27 21v6l4 3" stroke="#33a6d7" stroke-width="2" fill="none"/></svg>
    <h4>Care Schedule/Frequency</h4>
    <ul><li>Hearthside Home non medical visits require a four hour minimum visit.</li><li>There are no weekly minimums for medical or non medical visits.</li><li>Clients needing 24 hour care can save up to 30% off of services by using a live-in caregiver, with a scheduled break.</li></ul>
  </div>
  <div class="col" style="left:760px">
    <svg width="54" height="54"><circle cx="27" cy="27" r="26" fill="#e3f2fa"/><text x="27" y="34" text-anchor="middle" font-size="20" fill="#33a6d7" font-family="Roboto,sans-serif">$</text></svg>
    <h4>Payment Options</h4>
    <p class="p">Hearthside Home currently accepts private pay, long term care insurance and veterans benefits for in-home services.</p>
  </div>
</section>

<section class="testimonials">
  <div class="wrap eyebrow" style="top:62px">Testimonials</div>
  <div class="wrap title" style="top:82px;font-size:30px">Our <span>Patients Says About Us</span></div>
  <div class="photo" role="img" aria-label="Portrait of a patient" style="left:162px;top:192px;width:128px;height:123px;border-radius:50%;background:linear-gradient(135deg,#d8c3b0,#8a6a55)"></div>
  <div class="abs" style="left:318px;top:186px;font-size:40px;color:var(--blue);font-weight:700">❝</div>
  <p class="p abs" style="left:318px;top:228px;width:720px;font-size:12px;line-height:18px">Lorem ipsum dolor sit amet, consectetur adipiscing elit, sed do eiusmod tempor incididunt ut labore et dolore magna aliqua. Ut enim ad minim veniam, quis nostrud exercitation ullamco laboris nisi ut aliquip ex ea commodo consequat. Duis aute irure dolor in reprehenderit in voluptate velit esse cillum dolore eu fugiat nulla pariatur.</p>
  <div class="abs" style="left:318px;top:300px;font-size:14px;font-weight:500">Daniel Corwin</div>
  <div class="abs" style="left:318px;top:320px;font-size:11px;color:var(--blue)">Patient Professor</div>
  <div class="dots"><i></i><i></i><i></i></div>
</section>

<section class="consult">
  <div class="abs eyebrow" style="left:162px;top:64px;color:#fff">Consultation</div>
  <div class="abs" style="left:162px;top:82px;font-size:28px;font-weight:700">Free Consultation</div>
  <div class="legend" style="top:140px">CONTACT INFORMATION</div>
  <div class="field" style="left:162px;top:176px;width:190px">Full Name</div>
  <div class="field" style="left:370px;top:176px;width:192px">Phone Number</div>
  <div class="field" style="left:162px;top:222px;width:190px">Email Address</div>
  <div class="field" style="left:370px;top:222px;width:192px">Best Way to Reach You ▾</div>
  <div class="legend" style="top:274px">CLIENT INFORMATION</div>
  <div class="field" style="left:162px;top:310px;width:190px">Client Name</div>
  <div class="field" style="left:370px;top:310px;width:192px">Client Birthdate</div>
  <div class="field" style="left:162px;top:356px;width:190px">Address</div>
  <div class="field" style="left:370px;top:356px;width:192px">City</div>
  <div class="field" style="left:162px;top:402px;width:190px">State/Province</div>
  <div class="field" style="left:370px;top:402px;width:192px">Zip/Postal Code</div>
  <div class="field" style="left:162px;top:450px;width:400px;height:80px">Tell us more about the client and/or services that may be of interest to you *</div>
  <a class="btn abs" style="left:162px;top:550px;width:400px;text-align:center;background:#fff;color:var(--blue)">Submit Care Enquiry →</a>
</section>
<div class="photo" role="img" aria-label="Map of service towns with covered area highlighted in blue" style="left:682px;top:2505px;width:420px;height:425px;background:linear-gradient(135deg,#f2f4f7,#cfe0ef 50%,#3276b5)"></div>
<div class="stat" style="left:682px;width:148px"><b>19</b><span>Years of Experience</span></div>
<div class="stat" style="left:858px;width:244px"><b>1,200</b><span>Happy Patients</span></div>

<section>
  <div class="center eyebrow" style="top:3152px">Latest News &amp; Articles</div>
  <div class="center title" style="top:3172px;font-size:30px">Recent <span>Blog</span></div>
  <article class="post" style="left:162px"><div class="img" role="img" aria-label="Doctor holding stethoscope" style="background:linear-gradient(135deg,#f1ece6,#c44a3c)"></div><div class="date">19<small>October 2019</small></div><h3>Lorem ipsum dolor sit amet, consectetur adipiscing elit, sed do</h3><p class="p">Lorem ipsum dolor sit amet, consectetur adipiscing elit, sed do eiusmod tempor incididunt ut labore.</p><a class="btn">Read more →</a><span class="meta">✎ By Admin &nbsp; 0</span></article>
  <article class="post" style="left:462px"><div class="img" role="img" aria-label="Nurse caring for patient in bed" style="background:linear-gradient(135deg,#d9e8f2,#7fb1d2)"></div><div class="date">19<small>October 2019</small></div><h3>Lorem ipsum dolor sit amet, consectetur adipiscing elit, sed do</h3><p class="p">Lorem ipsum dolor sit amet, consectetur adipiscing elit, sed do eiusmod tempor incididunt ut labore.</p><a class="btn">Read more →</a><span class="meta">✎ By Admin &nbsp; 0</span></article>
  <article class="post" style="left:760px"><div class="img" role="img" aria-label="Caregiver walking with senior man" style="background:linear-gradient(135deg,#e8e0d4,#9a8468)"></div><div class="date">19<small>October 2019</small></div><h3>Lorem ipsum dolor sit amet, consectetur adipiscing elit, sed do</h3><p class="p">Lorem ipsum dolor sit amet, consectetur adipiscing elit, sed do eiusmod tempor incididunt ut labore.</p><a class="btn">Read more →</a><span class="meta">✎ By Admin &nbsp; 0</span></article>
  <a class="btn abs" style="left:520px;top:3706px;border:1px solid var(--blue);color:var(--blue)">Load more post</a>
</section>

<section class="cta">
  <div class="photo" role="img" aria-label="Nurse in white coat standing" style="left:190px;top:-48px;width:250px;height:253px;background:linear-gradient(180deg,#e9eef2,#2f6a8a)"></div>
  <div class="cta-box">If you need any home service<br>Feel free to call us 24hr emergency number<br><b>+88 555 01 47</b><a class="btn">Contact us →</a></div>
</section>

<footer class="site-footer">
  <div class="fcol" style="left:160px"><h5>SUBSCRIBE US</h5>Subscribe our newsletter to get latest news, updates and offers.<div class="sub-input">Your email Address</div><a class="btn" style="background:#fff;color:var(--blue);padding:6px 14px;font-size:10px">Submit</a></div>
  <div class="fcol" style="left:385px"><h5>SKILLED CARE SERVICES</h5>Free Initial Nursing Assessment<br>Medication Management<br>Wound Care<br>Injections<br>Medical Care Assistance<br>Transportation to Medical Appointments<br>Care Plan Management</div>
  <div class="fcol" style="left:610px"><h5>NON-MEDICAL SERVICES</h5>Live-in Care<br>Respite Care<br>Assisting with Daily Living Activities<br>Meal Preparation<br>Companionship<br>Homemaking</div>
  <div class="fcol" style="left:835px"><h5>GET IN TOUCH</h5>⌂ Hearthside Home Health Services<br>&nbsp;&nbsp;&nbsp;PO Box 412<br>&nbsp;&nbsp;&nbsp;Harbor, MA 02000<br><b style="color:#fff">✆ 781-555-0142</b><br>✉ contact@qtrblooms.com<br>◷ Monday-Friday 9:00am-5:00pm</div>
  <div class="fbar"><span style="color:#fff">Home</span> &nbsp;|&nbsp; About Us &nbsp;|&nbsp; Services &nbsp;|&nbsp; Testimonials &nbsp;|&nbsp; Blog &nbsp;|&nbsp; Contact
    <div class="social"><i></i><i></i><i></i><i></i></div>
    <div style="margin-top:24px;font-size:10px">© 2019 Hearthside Health &amp; Home Services. All rights reserved.</div>
  </div>
</footer>

</body>
</html>
```